Legal Agribusiness Capability Brochure Design

Design A4 sized 6 page Legal Agribusiness Capability Brochure. Design is to be consistent with current marketing materials - logo, letterhead, website and business card to be provided.
Cover page - Firm name and logo, Agribusiness Capability Statement heading with image 1 below
Inside cover page - About Us section with image 2 below then Awards section below image
Inside middle page - Our Expertise with image 3 below
Inside back page - Our Experience with image 4 below
Back page - Senior Lawyers with image 5 below
Outside Middle Back Page - Contact Us with image 6
Updates

To provide more details to designers for brochure

Target Market(s)

Agribusiness - Australia

Industry/Entity Type

Legal

Colors

Designer to choose colors to be used in the design.

Requirements
Must have
• Use content from uloaded file - Agribusiness Brochure Content
• Use images uploaded
• Professional appearance
• Consistent with current marketing and website https://ferngatelegal.com.au/

```html
<!DOCTYPE html>
<html lang="en">
<head>
<meta charset="utf-8">
<title>Ferngate Legal – Agribusiness Capability Statement</title>
<link href="https://fonts.googleapis.com/css2?family=Oswald:wght@400;500;600&family=Open+Sans:wght@400;600;700&display=swap" rel="stylesheet">
<style>
:root{
  --stage:#d6d6d8;
  --beige:#efe6d2;
  --white:#ffffff;
  --blue:#1b82c9;
  --ink:#3d3d3d;
  --heading-grey:#4d4d4d;
  --band:#616264;
}
*{box-sizing:border-box;margin:0;padding:0}
html,body{width:960px;height:1200px;overflow:hidden;background:var(--stage)}
body{position:relative;font-family:"Open Sans",Arial,sans-serif;color:var(--ink)}
.spread{position:absolute;left:24px;width:912px;box-shadow:0 2px 6px rgba(0,0,0,.25)}
.spread--outside{top:148px;height:430px;background:var(--beige)}
.spread--inside{top:600px;height:428px;background:var(--white)}
.band-top{position:absolute;left:0;top:0;width:100%;height:8px;background:var(--band)}
.band-bottom{position:absolute;left:0;bottom:0;width:100%;height:9px;background:var(--band)}
.panel{position:absolute;top:0;height:100%}
.block{position:absolute;left:0;width:100%}
.section-title{font-family:"Oswald",sans-serif;font-weight:500;color:var(--blue);font-size:15px;line-height:1;letter-spacing:.1px}
.body{font-size:5.4px;line-height:1.55;color:var(--ink)}
.body p{margin-bottom:4px;text-align:justify}
.bullets{list-style:none;font-size:5.4px;line-height:1.7}
.bullets li{position:relative;padding-left:17px}
.bullets li::before{content:"";position:absolute;left:2px;top:2.3px;width:3px;height:3px;border-radius:50%;background:var(--blue)}
.photo{position:absolute;border-radius:48px 0 48px 0;overflow:hidden}
.notch{position:absolute;left:50%;bottom:-1px;transform:translateX(-50%);width:0;height:0;border-left:8px solid transparent;border-right:8px solid transparent;border-bottom:12px solid var(--white)}
.notch--beige{border-bottom-color:var(--beige)}
.lawyer{position:relative;padding-left:58px;min-height:56px}
.portrait{position:absolute;left:0;top:0;width:54px;height:54px;background:linear-gradient(#f2f2f2,#8c8f96)}
.lawyer-name{font-family:"Oswald",sans-serif;font-weight:500;font-size:9.5px;color:var(--heading-grey);margin-bottom:3px}
.ranked{font-weight:700;color:var(--blue);font-size:6px;margin:2px 0 1px 2px}
.contact-title{font-family:"Oswald",sans-serif;font-weight:500;font-size:19px;color:var(--heading-grey);text-align:center}
.office{position:absolute;font-size:6px;line-height:1.45}
.office h4{font-weight:700;font-size:6.2px;margin-bottom:3px}
.url-bar{position:absolute;left:0;bottom:9px;width:100%;height:13px;background:var(--band);color:var(--white);font-weight:700;font-size:6.4px;letter-spacing:1.3px;text-align:center;line-height:13px}
.brand{position:absolute;left:60px;top:40px;display:flex;align-items:center;gap:8px}
.brand-mark{width:22px;height:22px;background:var(--blue)}
.brand-name{font-weight:600;font-size:17px;line-height:1;color:var(--blue);letter-spacing:.5px}
.brand-tag{font-size:7.5px;color:var(--heading-grey);margin-top:3px;font-weight:600}
.badge{position:absolute;top:94px;width:48px;height:48px;border-radius:50%}
.cover-title{position:absolute;left:0;width:304px;text-align:center;font-family:"Oswald",sans-serif;color:var(--blue);line-height:1;z-index:2}
.cover-title--main{top:150px;font-size:44px;font-weight:600;letter-spacing:-.3px}
.cover-title--sub{top:200px;font-size:21px;font-weight:500}
.sub-lead{font-weight:700;font-size:6.2px}
</style>
</head>
<body>

<section class="spread spread--outside">
  <div class="band-top"></div>

  <article class="panel" style="left:0;width:304px">
    <div style="position:absolute;left:20px;top:26px;width:264px">
      <h2 class="section-title" style="margin-bottom:6px">SENIOR LAWYERS</h2>
      <div class="lawyer">
        <div class="portrait" role="img" aria-label="Portrait of Tom Brenning in a dark suit"></div>
        <h3 class="lawyer-name">TOM BRENNING –PRINCIPAL</h3>
        <div class="body">
          <p>Tom has practiced exclusively as a commercial lawyer for over 20 years initially at Perth law firms and since 2009 in Geraldton.</p>
          <p>In 2011, Tom established Ferngate Legal in Geraldton and expanded with the opening of a Perth office in 2017.</p>
        </div>
      </div>
      <div class="body">
        <p>Tom has advised on a large number of commercial matters and disputes, particularly in relation to agribusiness, business, property, wills and estates. He has a proven track record of delivering results to clients, especially in relation to more complex commercial transactions and disputes.</p>
        <p>Tom has a specific interest in agribusiness, primarily due to his family being involved in agribusiness for several generations.</p>
      </div>
      <p class="ranked">Ranked by Lexley's Guides as:</p>
      <ul class="bullets" style="margin-bottom:6px">
        <li>"Preeminent Agribusiness Lawyer – Western Australia, 2019" (Top 2 in W.A.)</li>
        <li>"Leading Agribusiness Lawyer – Western Australia, 2018" (Top 5 in W.A.)</li>
        <li>"Leading Agribusiness Lawyer – Western Australia, 2017" (Top 7 in W.A.)</li>
      </ul>
      <div class="lawyer">
        <div class="portrait" role="img" aria-label="Portrait of Max Brenning in a dark suit"></div>
        <h3 class="lawyer-name">MAX BRENNING – CONSULTANT</h3>
        <div class="body">
          <p>Max was awarded a Bachelor of Laws from Westbrook University in 1973. Since then Max has been a partner at firms in Geraldton and Fremantle, as well as a principal of firms in Geraldton and Fremantle. In late 2009 Max and his wife, Anne, made the decision to move back to Geraldton where they had previously lived for approximately 11 years.</p>
        </div>
      </div>
      <div class="body"><p>Max has accumulated experience in a wide range of areas in over 45 years of legal practice, particularly in relation to Agribusiness disputes and litigation, which is of great benefit to his clients.</p></div>
    </div>
    <div class="photo" role="img" aria-label="Vineyard rows in autumn colours with a dirt track" style="left:42px;top:282px;width:222px;height:132px;background:linear-gradient(180deg,#9fc4e8 0%,#b9d3ea 18%,#7e4a2c 40%,#a5703f 65%,#c9a98a 100%)">
      <span class="notch notch--beige"></span>
    </div>
  </article>

  <article class="panel" style="left:304px;width:304px">
    <h2 class="contact-title" style="margin-top:32px">CONTACT US</h2>
    <p class="body" style="position:absolute;left:44px;top:70px;width:230px;font-size:6px">If you have any questions or require any assistance in relation to agribusiness law, please contact us at our Geraldton or Perth office.</p>
    <div class="office" style="left:44px;top:96px">
      <h4>Geraldton Office</h4>
      Suite 2, Harbour View House<br>12 Jetty Lane<br>Geraldton WA 6530<br>+61 8 9900 1120<br>+ 61 8 9900 1121<br>info@ferngatelegal.com.au
    </div>
    <div class="office" style="left:199px;top:96px">
      <h4>Perth Office</h4>
      18 Carrow Avenue<br>West Perth WA 6005<br>+61 8 9300 2230<br>+ 61 8 9300 2231<br>info@ferngatelegal.com.au
    </div>
    <div role="img" aria-label="Yellow combine harvester cutting a golden wheat crop under a hazy sky" style="position:absolute;left:0;top:198px;width:304px;height:232px;background:linear-gradient(180deg,#efe6d2 0%,#cfc3b0 25%,#a89984 50%,#c9a56a 70%,#b68a4a 100%)"></div>
    <div class="url-bar">https://ferngatelegal.com.au/</div>
  </article>

  <article class="panel" style="left:608px;width:304px">
    <div class="brand">
      <span class="brand-mark"></span>
      <div>
        <div class="brand-name">FERNGATE LEGAL</div>
        <div class="brand-tag">Commercial + Litigation</div>
      </div>
    </div>
    <div class="badge" style="left:82px;background:#d9c48a" role="img" aria-label="Ranking award badge"></div>
    <div class="badge" style="left:176px;background:#3a3a3a" role="img" aria-label="Quality practice certification badge"></div>
    <div role="img" aria-label="Flock of sheep standing on red dirt in a dry paddock" style="position:absolute;left:0;top:192px;width:304px;height:229px;background:linear-gradient(180deg,#efe6d2 0%,#d7c6a6 30%,#b08a5e 55%,#8a5a36 80%,#6e4429 100%)"></div>
    <h1 class="cover-title cover-title--main">AGRIBUSINESS</h1>
    <div class="cover-title cover-title--sub">CAPABILITY STATEMENT</div>
  </article>

  <div class="band-bottom"></div>
</section>

<section class="spread spread--inside">
  <div class="band-top"></div>

  <article class="panel" style="left:21px;width:262px">
    <h2 class="section-title block" style="top:29px">ABOUT US</h2>
    <ul class="bullets block" style="top:48px">
      <li>Independent commercial law firm with offices in Geraldton and Perth</li>
      <li>Senior lawyers offering a combined 65 years of legal experience</li>
      <li>Practical advice in a professional and timely manner</li>
      <li>Client relationships built on trust</li>
      <li>Unfettered access to senior lawyers</li>
      <li>Direct and ongoing partner level involvement for each client</li>
      <li>Utilise the best information technology available to maintain high levels of efficiency and confidentiality</li>
    </ul>
    <h2 class="section-title block" style="top:141px">AGRIBUSINESS LEGAL AWARDS</h2>
    <ul class="bullets block" style="top:160px">
      <li>Ranked as a "Leading Agribusiness Law Firm – Western Australia, 2019" (Top 4)</li>
      <li>Ranked as a "Leading Agribusiness Law Firm – Western Australia, 2018" (Top 4)</li>
      <li>Ranked as a "Leading Agribusiness Law Firm – Western Australia, 2017" (Top 5)</li>
    </ul>
    <h2 class="section-title block" style="top:203px">QUALITY PRACTICE STANDARD</h2>
    <p class="body block" style="top:219px;text-align:justify">We are part of a select group of law firms which has been awarded the Quality Practice Standard by the Coastal Practitioners Council. As a result, we are able to better serve our clients by:</p>
    <ul class="bullets block" style="top:238px">
      <li>Adopting modern quality management principles;</li>
      <li>Focusing on clients' requirements and client care; and</li>
      <li>Striving for consistency of service for all clients by all at the firm.</li>
    </ul>
    <div class="photo" role="img" aria-label="Yellow canola fields and green paddocks under a blue sky" style="left:21px;top:282px;width:222px;height:132px;background:linear-gradient(180deg,#6f9bc4 0%,#a9c4d8 28%,#8a9a5a 45%,#e4d23a 62%,#d9c92c 80%,#6e8a3a 100%)">
      <span class="notch"></span>
    </div>
  </article>

  <article class="panel" style="left:324px;width:266px">
    <h2 class="section-title block" style="top:29px">OUR EXPERTISE</h2>
    <div class="body block" style="top:48px">
      <p>Over several decades our senior lawyers have advised clients involved in wheat, canola, lupin, wool, beef, dairy, wool, lamb, poultry, piggery, viticulture, forestry and plantation businesses.</p>
      <p>Our senior lawyers have strong family connections with pastoralists which allows them to better appreciate the challenges faced in agribusiness.</p>
      <p>Our family connection with pastoralists and our strong technical expertise in agribusiness law places Ferngate Legal in a unique position to advise clients in the agribusiness industry.</p>
    </div>
    <p class="sub-lead block" style="top:127px">We can assist with the following agribusiness matters:</p>
    <ul class="bullets block" style="top:144px">
      <li>Agribusiness property contracts, agreements and deeds;</li>
      <li>Sale and purchase of agribusiness and farm assets;</li>
      <li>Pastoral lease advice;</li>
      <li>Native Title advice concerning access and compensation agreements;</li>
      <li>Land access agreements with mining, energy and telecommunications companies;</li>
      <li>Partnership, trust, corporation and joint venture advice;</li>
      <li>Farm Leases, Share Farming Agreements and Livestock Management Agreements;</li>
      <li>Carbon trading advice;</li>
      <li>Mortgages and securities;</li>
      <li>Farm succession planning, including Wills, Enduring Powers of Attorney and Guardianship;</li>
      <li>Employment advice;</li>
      <li>Deceased estates and probate, including advice concerning family provision claims; and</li>
      <li>Disputes.</li>
    </ul>
    <div class="photo" role="img" aria-label="Silhouetted stockman on horseback driving cattle through dust at sunset" style="left:21px;top:282px;width:222px;height:132px;background:radial-gradient(circle at 72% 25%,#f4efe0 0%,#b9ad92 18%,#5d5548 45%,#2b2620 80%)">
      <span class="notch"></span>
    </div>
  </article>

  <article class="panel" style="left:628px;width:266px">
    <h2 class="section-title block" style="top:29px">EXPERIENCE</h2>
    <div class="body block" style="top:48px">
      <p>Our senior lawyers have accumulated a wealth of experience in agribusiness law.</p>
      <p>Most of our work is subject to confidentiality which prevents us from disclosing any confidential information. However, we are able to disclose that our experience in agribusiness includes:</p>
    </div>
    <ul class="bullets block" style="top:82px;text-align:justify">
      <li>Advising clients with respect to the sale and acquisition of farmland, including due diligence enquiries, preparation and review of contracts for sale, registration of securities and settlement.</li>
      <li>Advising farmer in relation to the 180-megawatt Kellerby Wind Farm to be constructed on farmland near Eneabba, with a project value of up to AUD500 million and which is recognised as one of the best renewable projects in Australia.</li>
      <li>Advising pastoral lease holders on the sale and purchase of pastoral leases.</li>
      <li>Advising client on the termination of a vendor terms agreement for the sale of a farm and the repossession and resale of the farm.</li>
      <li>Advising numerous clients on various agreements with mining companies, including Royalty Agreements, Exploration Agreements, Land Access Deeds, Leases, Transmission Line Works Agreements, Deeds of Settlement and Release, Easement Deeds and Lay-Down Area Agreements.</li>
      <li>Advising on Access and Compensation Agreements with native title claimants.</li>
      <li>Advising client in relation to restructure of farmland and the transfer of the farmland to family members, trusts and a SMSF to qualify for the duties exemption under the Duties Act.</li>
      <li>Advising client in relation to the settlement of a farming partnership and trust dispute.</li>
      <li>Advising various farming families / corporate groups in relation to the restructuring of farm assets and exempt family farm transactions under the Duties Act.</li>
      <li>Advising farmers in relation to estate disputes and claims, including claims in the Supreme Court under the Family Provision Act.</li>
    </ul>
    <div class="photo" role="img" aria-label="Outback sunset with a windmill silhouette and red sky" style="left:20px;top:282px;width:222px;height:132px;background:linear-gradient(180deg,#5b7fa8 0%,#c98a6a 35%,#f29a32 58%,#e5641e 72%,#5a2414 100%)">
      <span class="notch"></span>
    </div>
  </article>

  <div class="band-bottom"></div>
</section>

</body>
</html>
```